Wine Label: Tressivo

The project is to create 3 wine labels. The brand name is "Tressivo"

What we need is to have 3 versions: red wine, white wine and rose.

The wine is for young and modern people, between 21 and 31 years old, so it need to be casual, modern and fun, but at the same time it needs to keep the Premiums of a good European wine.

It is from Italy.

Target Market(s)

Young adults, between 21 and 31 years old. wine lovers

Requirements
Must have
• - Modern colors (Black, silver, red, etc.)
• - Clean label
• - Clear font
• - Style
• - The brand + the type of wine (red, white or rose)
Nice to have
• - A symbol to represent the brand
Should not have
• - Many elements
• - No clear fonts
• - No funny colors

```html
<!DOCTYPE html>
<html lang="en">
<head>
<meta charset="utf-8">
<title>Tressivo — Wine Labels</title>
<link rel="stylesheet" href="https://fonts.googleapis.com/css2?family=Pinyon+Script&family=Cinzel:wght@400;600&family=Open+Sans:wght@600&display=swap">
<style>
  :root {
    --backdrop: #b9b97f;
    --red-label: #7d1519;
    --white-label: #050505;
    --rose-label: #c180b9;
    --ink: #ffffff;
    --vine-red: #a95a5c;
    --vine-white: #5a5a5a;
    --vine-rose: #dcb3d6;
  }
  * { margin: 0; padding: 0; box-sizing: border-box; }
  html, body {
    width: 1200px;
    height: 851px;
    overflow: hidden;
  }
  body {
    background: var(--backdrop);
    display: flex;
    align-items: center;
    justify-content: center;
    gap: 60px;
  }
  .label {
    position: relative;
    width: 330px;
    height: 690px;
    color: var(--ink);
  }
  .label--red { background: var(--red-label); --vine: var(--vine-red); }
  .label--white { background: var(--white-label); --vine: var(--vine-white); }
  .label--rose { background: var(--rose-label); --vine: var(--vine-rose); }

  .label__frame {
    position: absolute;
    inset: 28px 30px 30px 30px;
    border: 4px dotted var(--ink);
  }
  .label__corner {
    position: absolute;
    width: 12px;
    height: 12px;
    background: var(--ink);
  }
  .label__corner--tl { top: 22px; left: 24px; }
  .label__corner--tr { top: 22px; right: 24px; }
  .label__corner--bl { bottom: 24px; left: 24px; }
  .label__corner--br { bottom: 24px; right: 24px; }

  .label__brand {
    position: absolute;
    top: 78px;
    left: 0;
    right: 0;
    text-align: center;
    font-family: "Pinyon Script", cursive;
    font-size: 54px;
    line-height: 1;
  }
  .label__band {
    position: absolute;
    top: 168px;
    left: 0;
    right: 0;
    height: 14px;
    background: var(--ink);
  }
  .label__type {
    position: absolute;
    top: 198px;
    left: 0;
    right: 0;
    text-align: center;
    font-family: "Cinzel", serif;
    font-size: 24px;
    letter-spacing: 2px;
  }
  .label__details {
    position: absolute;
    top: 236px;
    left: 0;
    right: 0;
    text-align: center;
    font-family: "Open Sans", sans-serif;
    font-weight: 600;
    font-size: 14px;
    line-height: 1.35;
  }
  .label__vine {
    position: absolute;
    top: 300px;
    left: 52px;
    width: 200px;
    height: 300px;
    background: var(--vine);
    border-radius: 6px;
  }
</style>
</head>
<body>
  <section class="label label--red" aria-label="Tressivo red wine label">
    <div class="label__frame"></div>
    <span class="label__corner label__corner--tl"></span>
    <span class="label__corner label__corner--tr"></span>
    <span class="label__corner label__corner--bl"></span>
    <span class="label__corner label__corner--br"></span>
    <h2 class="label__brand">Tressivo</h2>
    <div class="label__band"></div>
    <p class="label__type">Wine Bottle</p>
    <p class="label__details">Details of the product<br>will be inserted here</p>
    <div class="label__vine" role="img" aria-label="White grape vine illustration with leaf, grape cluster and curling tendrils"></div>
  </section>

  <section class="label label--white" aria-label="Tressivo white wine label">
    <div class="label__frame"></div>
    <span class="label__corner label__corner--tl"></span>
    <span class="label__corner label__corner--tr"></span>
    <span class="label__corner label__corner--bl"></span>
    <span class="label__corner label__corner--br"></span>
    <h2 class="label__brand">Tressivo</h2>
    <div class="label__band"></div>
    <p class="label__type">Wine Bottle</p>
    <p class="label__details">Details of the product<br>will be inserted here</p>
    <div class="label__vine" role="img" aria-label="White grape vine illustration with leaf, grape cluster and curling tendrils"></div>
  </section>

  <section class="label label--rose" aria-label="Tressivo rosé wine label">
    <div class="label__frame"></div>
    <span class="label__corner label__corner--tl"></span>
    <span class="label__corner label__corner--tr"></span>
    <span class="label__corner label__corner--bl"></span>
    <span class="label__corner label__corner--br"></span>
    <h2 class="label__brand">Tressivo</h2>
    <div class="label__band"></div>
    <p class="label__type">Wine Bottle</p>
    <p class="label__details">Details of the product<br>will be inserted here</p>
    <div class="label__vine" role="img" aria-label="White grape vine illustration with leaf, grape cluster and curling tendrils"></div>
  </section>
</body>
</html>
```